Professional digital stationary

We need a digital stationary for our brand, we already have a logo and based on that we need a design for Word, Powerpoint, mailings and Linkedin. We need to be able to re use the stationary for other things like other social media. So basically what we ask is a template for Powerpoint and Word, some e-mail headers and a nice and professional Linkedin Header.

Target Market(s)

recruitment

Font styles to use
Sans Serif

```html
<!DOCTYPE html>
<html lang="en">
<head>
<meta charset="utf-8">
<title>Talentra – Presentation Template</title>
<link href="https://fonts.googleapis.com/css2?family=Questrial&display=swap" rel="stylesheet">
<style>
  :root {
    --bg: #d4d5d8;
    --paper: #ffffff;
    --blue: #3a6ea5;
    --blue-light: #6ea8e6;
    --blue-dark: #2f5f93;
    --grey-tri: #8a8a8a;
    --grey-light: #c9c9c9;
    --placeholder: #dcdcdc;
    --ink: #222222;
    --text-grey: #777777;
    --mark: #5b5b5b;
  }
  * { margin: 0; padding: 0; box-sizing: border-box; }
  html, body { width: 1200px; height: 1200px; overflow: hidden; }
  body {
    background: var(--bg);
    font-family: "Questrial", sans-serif;
    color: var(--ink);
    position: relative;
  }
  .slide {
    position: absolute;
    width: 350px; height: 196px;
    background: var(--paper);
    box-shadow: 0 2px 5px rgba(0,0,0,.18);
    overflow: hidden;
  }
  .slide > * { position: absolute; }
  .bar { background: var(--blue); height: 6px; }
  .title { color: var(--blue); font-size: 11px; line-height: 1.25; }
  .body-tiny { font-size: 3.4px; line-height: 1.35; color: var(--ink); }
  .body-small { font-size: 5.6px; line-height: 1.5; color: var(--ink); }
  .photo {
    background: radial-gradient(ellipse at 55% 55%, #8a6a2e 0%, #4a3a1c 22%, #151515 55%, #0c0c0c 100%);
  }
  .photo-caption { position: absolute; left: 0; right: 0; bottom: 0; height: 8px; background: #2b2f3a; }
  .wordmark { color: var(--mark); font-size: 16px; line-height: 1; letter-spacing: -.3px; }
  .wordmark small { display: block; font-size: 3px; letter-spacing: 0; color: var(--ink); margin-top: 1px; }
  .label { font-size: 5px; }
  .label.blue { color: var(--blue); }
  .label.light { color: var(--blue-light); }
  .label.grey { color: var(--text-grey); }
  .label.silver { color: #aaaaaa; }
  .placeholder { background: var(--placeholder); }
  .bullet::before {
    content: ""; position: absolute; left: -8px; top: 1px;
    width: 3px; height: 3px; background: var(--blue);
  }
</style>
</head>
<body>

<!-- Cover -->
<section class="slide" style="left:64px;top:290px">
  <div class="bar" style="left:0;top:56px;width:38px"></div>
  <div class="wordmark" style="left:42px;top:42px;font-size:38px">Talentra</div>
  <div class="body-small" style="left:43px;top:82px;font-size:8.5px">The right people, right now</div>
  <div class="body-small" style="left:76px;top:130px;width:160px">Lorem ipsum dolor sit amet, consectetuer adipiscing elit, sed diam nonummy nibh euismod</div>
  <div class="photo" role="img" aria-label="Photo of golden eggs in a nest, retirement planning theme" style="left:229px;top:0;width:121px;height:196px"><div class="photo-caption"></div></div>
</section>

<!-- Image + text -->
<section class="slide" style="left:426px;top:290px">
  <div class="bar" style="left:0;top:32px;width:50px;height:7px"></div>
  <div class="photo" role="img" aria-label="Retirement planning cover photo with golden eggs in a nest" style="left:0;top:58px;width:184px;height:124px"><div class="photo-caption"></div></div>
  <div class="title" style="left:221px;top:62px">Lorem Ipsum</div>
  <div class="body-tiny" style="left:221px;top:84px;width:80px">Lorem ipsum dolor sit amet, consectetuer adipiscing elit, sed diam nonummy nibh euismod tincidunt ut laoreet dolore magna aliquam erat volutpat. Ut wisi enim ad minim veniam, quis nostrud exerci tation ullamcorper suscipit lobortis nisl ut aliquip ex ea commodo consequat. Duis autem vel eum iriure dolor in hendrerit in vulputate velit esse molestie consequat, vel illum dolore eu feugiat nulla facilisis at vero eros et accumsan et iusto odio dignissim qui blandit praesent luptatum zzril delenit augue duis dolore te feugait nulla facilisi.</div>
  <div class="wordmark" style="left:267px;top:171px">Talentra<small>The right people, right now</small></div>
</section>

<!-- Process chart -->
<section class="slide" style="left:788px;top:290px">
  <div class="title" style="left:32px;top:34px">Graphic Chart</div>
  <div class="bar" style="left:299px;top:32px;width:51px"></div>
  <svg style="left:0;top:0" width="350" height="196" viewBox="0 0 350 196" fill="none" stroke="#555" stroke-width=".8">
    <path d="M56 68h5l8-5v14l-8-5h-5z M58 72v5h3v-5"/>
    <path d="M71 66l3-2 M71 70h4 M71 74l3 2"/>
    <rect x="134" y="60" width="19" height="13" rx="1"/>
    <path d="M138 67h11 M138 70h11 M141 76h5 M143.5 73v3"/>
    <path d="M213 79h22 M216 79v-6h3v6 M221 79v-9h3v9 M226 79v-12h3v12 M214 71l6-4 5 2 8-7"/>
    <g stroke="var(--blue)" stroke-width=".6">
      <path d="M35 92h62l15 15-15 15H35l15-15z"/>
      <path d="M113 92h62l15 15-15 15h-62l15-15z"/>
      <path d="M191 92h62l15 15-15 15h-62l15-15z"/>
    </g>
  </svg>
  <div class="body-tiny" style="left:57px;top:99px;width:42px">Lorem ipsum dolor sit amet, consectetuer adipiscing elit, sed diam nonummy nibh</div>
  <div class="body-tiny" style="left:135px;top:99px;width:42px">Lorem ipsum dolor sit amet, consectetuer adipiscing elit, sed diam nonummy nibh</div>
  <div class="body-tiny" style="left:213px;top:99px;width:42px">Lorem ipsum dolor sit amet, consectetuer adipiscing elit, sed diam nonummy nibh</div>
  <div class="body-tiny" style="left:35px;top:151px;width:92px">Lorem ipsum dolor sit amet, consectetuer adipiscing elit, sed diam nonummy nibh euismod tincidunt ut laoreet dolore magna aliquam erat volutpat. Ut wisi enim ad minim veniam, quis.</div>
  <div class="body-tiny" style="left:138px;top:151px;width:92px">Lorem ipsum dolor sit amet, consectetuer adipiscing elit, sed diam nonummy nibh euismod tincidunt ut laoreet dolore magna aliquam erat volutpat. Ut wisi enim ad minim veniam, quis.</div>
  <div class="wordmark" style="left:267px;top:171px">Talentra<small>The right people, right now</small></div>
</section>

<!-- Ring chart -->
<section class="slide" style="left:64px;top:497px">
  <div class="bar" style="left:0;top:36px;width:48px;height:7px"></div>
  <div class="title" style="left:79px;top:44px">Graphic Chart</div>
  <div class="body-tiny" style="left:210px;top:42px;width:92px">Lorem ipsum dolor sit amet, consectetuer adipiscing elit, sed diam nonummy nibh euismod tincidunt ut laoreet dolore magna aliquam erat volutpat. Ut wisi enim ad minim veniam, quis nostrud exerci tation ullamcorper suscipit lobortis.</div>
  <svg style="left:0;top:0" width="350" height="196" viewBox="0 0 350 196" fill="none" stroke-width="1.6">
    <g font-family="Questrial, sans-serif" font-size="5.5" fill="#333" stroke="none" text-anchor="middle">
      <text x="107" y="115">80%</text><text x="166" y="115">50%</text><text x="224" y="115">70%</text><text x="282" y="115">60%</text>
    </g>
    <path d="M107 89a24 24 0 1 1 -22.8 16.6" stroke="var(--blue)"/>
    <path d="M166 89a24 24 0 0 0 0 48" stroke="var(--grey-light)"/>
    <path d="M224 89a24 24 0 1 1 -19.4 38.1" stroke="var(--blue-light)"/>
    <path d="M282 89a24 24 0 1 1 -14.1 43.4" stroke="var(--grey-tri)"/>
  </svg>
  <div class="label blue" style="left:91px;top:145px">Graphic Chart</div>
  <div class="label silver" style="left:150px;top:145px">Graphic Chart</div>
  <div class="label light" style="left:208px;top:145px">Graphic Chart</div>
  <div class="label grey" style="left:266px;top:145px">Graphic Chart</div>
  <div class="body-tiny" style="left:93px;top:154px;width:30px;text-align:center">Lorem ipsum dolor sit amet, consectetuer adipiscing elit,</div>
  <div class="body-tiny" style="left:152px;top:154px;width:30px;text-align:center">Lorem ipsum dolor sit amet, consectetuer adipiscing elit,</div>
  <div class="body-tiny" style="left:210px;top:154px;width:30px;text-align:center">Lorem ipsum dolor sit amet, consectetuer adipiscing elit,</div>
  <div class="body-tiny" style="left:268px;top:154px;width:30px;text-align:center">Lorem ipsum dolor sit amet, consectetuer adipiscing elit,</div>
</section>

<!-- Bullets + image -->
<section class="slide" style="left:426px;top:497px">
  <div class="photo" role="img" aria-label="Retirement planning cover photo with golden eggs in a nest" style="left:177px;top:24px;width:150px;height:131px"><div class="photo-caption"></div></div>
  <div class="bar" style="left:327px;top:25px;width:23px"></div>
  <div class="title" style="left:33px;top:92px">Lorem Ipsum</div>
  <div class="body-tiny bullet" style="left:43px;top:116px;width:80px">Lorem ipsum dolor sit amet, consectetuer adipiscing elit, sed diam nonummy nibh euismod tincidunt ut laoreet dolore magna aliquam erat volutpat.</div>
  <div class="body-tiny bullet" style="left:43px;top:138px;width:80px">Lorem ipsum dolor sit amet, consectetuer adipiscing elit, sed diam nonummy nibh euismod tincidunt ut laoreet dolore magna aliquam erat volutpat.</div>
  <div class="body-tiny bullet" style="left:43px;top:160px;width:80px">Lorem ipsum dolor sit amet, consectetuer adipiscing elit, sed diam nonummy nibh euismod tincidunt ut laoreet dolore magna aliquam erat volutpat.</div>
</section>

<!-- Text + tall image -->
<section class="slide" style="left:788px;top:497px">
  <div class="bar" style="left:0;top:24px;width:50px;height:7px"></div>
  <div class="title" style="left:22px;top:62px">Lorem<br>Ipsum</div>
  <div class="body-tiny" style="left:95px;top:62px;width:64px">Lorem ipsum dolor sit amet, consectetuer adipiscing elit, sed diam nonummy nibh euismod tincidunt ut laoreet dolore magna aliquam erat volutpat. Ut wisi enim ad minim veniam, quis nostrud exerci tation ullamcorper suscipit lobortis nisl ut aliquip ex ea commodo consequat. Duis autem vel eum iriure dolor in hendrerit in vulputate velit esse molestie consequat, vel illum dolore eu feugiat nulla facilisis at vero eros et accumsan et iusto odio dignissim qui blandit praesent luptatum zzril delenit.</div>
  <div class="photo" role="img" aria-label="Retirement planning cover photo with golden eggs in a nest" style="left:187px;top:0;width:163px;height:149px"><div class="photo-caption"></div></div>
  <div style="left:187px;top:149px;width:163px;height:47px;background:#dedede"></div>
  <div class="wordmark" style="left:267px;top:171px">Talentra<small>The right people, right now</small></div>
</section>

<!-- Three placeholders -->
<section class="slide" style="left:64px;top:705px">
  <div class="placeholder" role="img" aria-label="Image placeholder" style="left:28px;top:33px;width:61px;height:71px"></div>
  <div class="placeholder" role="img" aria-label="Image placeholder" style="left:98px;top:33px;width:61px;height:71px"></div>
  <div class="placeholder" role="img" aria-label="Image placeholder" style="left:168px;top:33px;width:61px;height:71px"></div>
  <div class="label blue" style="left:27px;top:120px">Graphic Chart</div>
  <div class="label blue" style="left:97px;top:120px">Graphic Chart</div>
  <div class="label blue" style="left:167px;top:120px">Graphic Chart</div>
  <div class="body-tiny" style="left:27px;top:130px;width:50px">Lorem ipsum dolor sit amet, consectetuer adipiscing elit, sed diam nonummy nibh euismod tincidunt ut laoreet dolore magna aliquam erat volutpat.</div>
  <div class="body-tiny" style="left:97px;top:130px;width:50px">Lorem ipsum dolor sit amet, consectetuer adipiscing elit, sed diam nonummy nibh euismod tincidunt ut laoreet dolore magna aliquam erat volutpat.</div>
  <div class="body-tiny" style="left:167px;top:130px;width:50px">Lorem ipsum dolor sit amet, consectetuer adipiscing elit, sed diam nonummy nibh euismod tincidunt ut laoreet dolore magna aliquam erat volutpat.</div>
  <div class="bar" style="left:299px;top:31px;width:51px"></div>
  <div class="title" style="left:282px;top:80px">Lorem<br>Ipsum</div>
  <div class="wordmark" style="left:265px;top:171px">Talentra<small>The right people, right now</small></div>
</section>

<!-- Triangle chart -->
<section class="slide" style="left:426px;top:705px">
  <div class="bar" style="left:0;top:32px;width:50px;height:7px"></div>
  <div class="title" style="left:66px;top:30px">Graphic Chart</div>
  <div class="body-tiny bullet" style="left:219px;top:34px;width:92px">Lorem ipsum dolor sit amet, consectetuer adipiscing elit, sed diam nonummy nibh euismod tincidunt ut laoreet dolore magna aliquam erat volutpat.</div>
  <svg style="left:0;top:0" width="350" height="196" viewBox="0 0 350 196">
    <polygon points="82,152 113,99 142,152" fill="var(--grey-tri)" opacity=".95"/>
    <polygon points="124,152 162,78 201,152" fill="var(--blue-light)" opacity=".9"/>
    <polygon points="176,152 209,99 242,152" fill="var(--grey-light)" opacity=".85"/>
    <polygon points="219,152 245,107 270,152" fill="var(--blue-dark)" opacity=".85"/>
    <g font-family="Questrial, sans-serif" font-size="5.5" fill="#333" text-anchor="middle">
      <text x="115" y="93">70%</text><text x="163" y="72">80%</text>
      <text x="210" y="93">60%</text><text x="246" y="100">50%</text>
    </g>
  </svg>
  <div class="label grey" style="left:91px;top:160px">Graphic Chart</div>
  <div class="label light" style="left:143px;top:160px">Graphic Chart</div>
  <div class="label silver" style="left:191px;top:160px">Graphic Chart</div>
  <div class="label blue" style="left:244px;top:160px">Graphic Chart</div>
</section>

<!-- Icon list -->
<section class="slide" style="left:788px;top:705px">
  <div class="title" style="left:25px;top:50px;font-size:12px">Lorem<br>Ipsum</div>
  <svg style="left:0;top:0" width="350" height="196" viewBox="0 0 350 196" fill="none" stroke-width=".7">
    <g stroke="#d0d0d0"><circle cx="94" cy="56" r="8"/><circle cx="94" cy="94" r="8"/><circle cx="94" cy="134" r="8"/></g>
    <g stroke="var(--blue)">
      <path d="M89 57l5-5 5 5 M90.5 56v4.5h7V56 M93 60.5v-2.5h2v2.5"/>
      <path d="M91 89h6 M91 99h6 M92 89c0 3 4 3 4 5s-4 2-4 5 M96 89c0 3-4 3-4 5s4 2 4 5"/>
      <path d="M89 132l5-3 5 3v5h-10z M89 132l5 3 5-3"/>
    </g>
  </svg>
  <div class="label blue" style="left:111px;top:51px">Lorem Ipsum</div>
  <div class="body-tiny" style="left:111px;top:59px;width:50px">Lorem ipsum dolor sit amet, consectetuer adipiscing elit, sed diam nonummy nibh euismod tincidunt ut laoreet dolore magna aliquam erat volutpat.</div>
  <div class="label blue" style="left:111px;top:90px">Lorem Ipsum</div>
  <div class="body-tiny" style="left:111px;top:98px;width:50px">Lorem ipsum dolor sit amet, consectetuer adipiscing elit, sed diam nonummy nibh euismod tincidunt ut laoreet dolore magna aliquam erat volutpat.</div>
  <div class="label blue" style="left:111px;top:130px">Lorem Ipsum</div>
  <div class="body-tiny" style="left:111px;top:138px;width:50px">Lorem ipsum dolor sit amet, consectetuer adipiscing elit, sed diam nonummy nibh euismod tincidunt ut laoreet dolore magna aliquam erat volutpat.</div>
  <div class="placeholder" role="img" aria-label="Image placeholder" style="left:202px;top:23px;width:110px;height:94px"></div>
  <div class="bar" style="left:0;top:147px;width:50px;height:7px"></div>
  <div class="wordmark" style="left:267px;top:171px">Talentra<small>The right people, right now</small></div>
</section>

</body>
</html>
```